New webpage for Facility Management Company (cleaning services)

We need a new web page design for a company based in Stockholm, Sweden, called TKR Clean AB (established 1991). We provide cleaning services to the public sector, to businesses, and to home owners. Our services primarily include daily cleaning, floor care, window cleaning, and carpet cleaning.

Our company holds certificates for ISO 9001, ISO 14001, ISO 45001 and "Hjorten".

Referring to "the Swedish model" we honor collective agreements between Veltrio (employer-representative organisation and relevant labour unions (e.g. Arbetsfront).
The final design should communicate that we are a trustworthy company with a well trained staff, high quality services combined with a commitment to run a sustainable business from a labour and environmental perspective.

DETAILS
General
-----------------------------------------------
• Language: Swedish (we provide text)
• Very important: Easy to administrate for company staff without special technical skills, especially to
o add/change information about HQ staff
o change any text
o add/change information about offered services
• Responsive
• SEO-friendly

Content that web page needs to cover in one way or the other
--------------------------------------------
• Information about our company
• About our staff and contact info to HQstaff/management (photos, contact info)
• Our ambitions and supporting info (quality, environment, labour conditions, certificates, etc)
• Information to customers within the public sector
• Information to customers within the private sector
• Information to customers within the home owner sector
• Services public sector (Swedish = Offentlig sektor)
• Services private business sector (Swedish = Företag) Se törnvall
• Services home owner sector (Swedish=Privat)
• GDPR compliance
• News

Content/Function
-------------------------------
• One specific requirement is that we need a page for information to potentially new employees (some general information and open job positions) with a possibility to fill in a simple application form and upload CV.(Mail?) CAPTCHA or equivalent.
• Contact form for customers with CAPTCHA or equivalent.
• Cookie management
• Integration social media (future); easy to manage/add/delete integration of social media.

We are not interested in a blog at this point of time

```html
<!DOCTYPE html>
<html lang="sv">
<head>
<meta charset="utf-8">
<title>TKR Clean AB – Städtjänster i Stockholm</title>
<link href="https://fonts.googleapis.com/css2?family=Rubik:wght@400;500;700&family=Roboto+Condensed:wght@400;700&family=Poppins:wght@400;500&display=swap" rel="stylesheet">
<style>
:root{
  --green:#4db848;
  --green-dark:#3a9c36;
  --blue:#1581cf;
  --blue-dark:#0c62ad;
  --blue-light:#1c97e0;
  --navy:#1d2f4d;
  --text:#333;
  --muted:#666;
  --grey-bg:#eef1f5;
  --white:#fff;
}
*{box-sizing:border-box;margin:0;padding:0}
html,body{width:1200px;height:5329px;overflow:hidden}
body{font-family:"Poppins",sans-serif;color:var(--text);background:var(--white);position:relative}
.abs{position:absolute}
section,header,footer{position:absolute;left:0;width:1200px}
a{text-decoration:none}

/* header */
.site-header{top:0;height:118px;background:var(--white)}
.topbar{position:absolute;left:445px;top:0;width:683px;height:45px;background:var(--blue-light);border-bottom-left-radius:22px;display:flex;align-items:center;gap:20px;padding-left:22px;color:#fff;font-size:13px;white-space:nowrap}
.topbar .social{display:flex;gap:10px;margin-left:auto;margin-right:26px}
.dot{width:24px;height:24px;border-radius:50%;background:#fff;display:inline-block}
.logo{position:absolute;display:flex;align-items:center;gap:10px;font-family:"Rubik",sans-serif;font-weight:500;color:var(--navy);white-space:nowrap}
.logo .mark{border-radius:50%;background:var(--green)}
.nav{position:absolute;top:70px;left:545px;display:flex;gap:55px;font-family:"Rubik",sans-serif;font-size:17px;color:#222;white-space:nowrap}
.nav a{display:block;padding:0 0 18px;position:relative;color:inherit}
.nav a.active::after{content:"";position:absolute;left:-10px;right:-10px;bottom:0;height:4px;background:var(--green)}

/* hero */
.hero{top:118px;height:700px;overflow:hidden}
.hero-photo{position:absolute;inset:0;background:linear-gradient(100deg,#4a4c4f 0%,#6b6d70 45%,#8a8985 70%,#55575a 100%)}
.hero h1{position:absolute;left:100px;top:140px;font-family:"Rubik",sans-serif;font-weight:700;font-size:58px;line-height:80px;color:#fff;white-space:nowrap}
.btn{display:flex;align-items:center;justify-content:space-between;color:#fff;font-family:"Rubik",sans-serif;font-size:17px;padding:0 26px}
.hero .btn{position:absolute;top:424px;height:62px}
.btn-green{background:var(--green)}
.btn-blue{background:var(--blue-light)}
.arrow-line{width:40px;height:12px}
.dots{position:absolute;left:100px;top:580px;display:flex;gap:14px}
.dots span{width:12px;height:12px;border-radius:50%;border:2px solid #fff}
.dots span.on{background:var(--blue-light);border-color:var(--blue-light)}
.hero svg.wave{position:absolute;left:0;bottom:0}

/* headings */
.sec-title{font-family:"Rubik",sans-serif;font-weight:500;color:var(--green);text-transform:uppercase;text-align:center;font-size:40px;letter-spacing:.5px}
.sec-sub{text-align:center;font-size:17px;color:#333}
.hand-icon{display:block;margin:0 auto}
p.body{font-size:12.5px;line-height:19px;color:#444;text-align:justify}

/* about */
.about{top:818px;height:506px}
.about-photo{position:absolute;left:100px;top:72px;width:396px;height:396px;border-radius:50%;background:linear-gradient(135deg,#1f5f9c,#4a94cf 50%,#2a6da8)}
.about-ring{position:absolute;left:92px;top:64px}
.about-text{position:absolute;left:551px;top:96px;width:553px}
.about-text h2{font-family:"Rubik",sans-serif;font-weight:500;color:var(--blue-light);font-size:38px;line-height:44px}
.about-text h3{font-family:"Rubik",sans-serif;font-weight:400;font-size:24px;color:#222;margin:4px 0 18px}
.about-text p{margin-bottom:16px}
.btn-sm{display:inline-flex;align-items:center;gap:22px;background:var(--blue-light);color:#fff;font-family:"Rubik",sans-serif;font-size:14px;height:40px;padding:0 20px}

/* staff */
.staff{top:1324px;height:600px;background:var(--grey-bg)}
.staff-cards{position:absolute;left:100px;top:280px;display:flex;gap:14px}
.card{width:243px;height:264px;background:#fff;border:1px solid #d9dde3;text-align:center;padding-top:18px}
.avatar{width:132px;height:132px;border-radius:50%;margin:0 auto;border:5px solid var(--blue-light);background:linear-gradient(180deg,#d7dde3,#a9b3bd)}
.card h4{font-family:"Roboto Condensed",sans-serif;font-weight:700;color:var(--blue-light);font-size:19px;margin-top:14px;text-transform:uppercase}
.card .role,.card .tel{font-size:10px;color:#777;line-height:14px}
.card .socials{display:flex;gap:5px;justify-content:center;margin-top:8px}
.card .socials span{width:19px;height:19px;border-radius:50%;background:var(--green)}
.chev{position:absolute;top:395px}

/* services */
.services{top:1924px;height:807px;overflow:hidden}
.services-bg{position:absolute;inset:0;background:linear-gradient(90deg,var(--blue-dark),var(--blue-light) 55%,var(--blue))}
.services .sec-title,.services .sec-sub{color:#fff}
.svc{position:absolute;top:330px;width:210px;text-align:center;color:#fff}
.svc-photo{width:200px;height:200px;border-radius:50%;border:4px solid #fff;margin:0 auto;background:linear-gradient(160deg,#e8edf2,#9aa7b3)}
.svc-icon{width:62px;height:62px;border-radius:50%;background:var(--blue-light);border:3px solid #fff;margin:-52px auto 0;position:relative;display:flex;align-items:center;justify-content:center}
.svc h3{font-family:"Rubik",sans-serif;font-weight:500;font-size:24px;line-height:30px;margin-top:10px}
.svc .more{display:inline-flex;align-items:center;gap:20px;margin-top:22px;background:var(--green);border-radius:22px;height:42px;padding:0 8px 0 22px;font-family:"Rubik",sans-serif;font-size:14px;color:#fff}
.svc .more i{width:26px;height:26px;border-radius:50%;background:#fff;display:flex;align-items:center;justify-content:center}

/* ambitions */
.ambitions{top:2731px;height:476px;background:#f4f6f8}
.amb-cards{position:absolute;left:100px;top:228px;display:flex;gap:17px}
.amb{width:237px;height:192px;background:#fff;border-radius:10px;box-shadow:0 2px 8px rgba(0,0,0,.08);text-align:center;padding-top:30px;font-family:"Rubik",sans-serif;font-size:19px;color:#222}
.amb svg{display:block;margin:0 auto 14px}

/* sectors */
.sector{position:absolute;width:500px}
.sector h2{font-family:"Rubik",sans-serif;font-weight:500;font-size:38px;color:var(--blue-light);margin-bottom:14px;white-space:nowrap}
.sector p{margin-bottom:16px}
.sector-photo{position:absolute;width:502px;height:308px}

/* jobs */
.jobs{top:4334px;height:538px}
.jobs-left{position:absolute;left:0;top:0;width:600px;height:538px;background:var(--blue-light)}
.jobs-right{position:absolute;left:600px;top:0;width:600px;height:538px;background:var(--green)}
.panel-title{position:absolute;display:flex;align-items:center;gap:14px;font-family:"Rubik",sans-serif;font-weight:500;font-size:38px;color:#fff;white-space:nowrap}
.job{position:absolute;left:100px;width:440px;color:#fff}
.job .num{position:absolute;left:0;top:-6px;font-family:"Rubik",sans-serif;font-size:42px;font-weight:400}
.job h4{margin-left:48px;font-family:"Rubik",sans-serif;font-weight:500;font-size:24px}
.job p{margin-left:48px;font-size:10.5px;line-height:15px;margin-top:2px}
.apply{display:inline-flex;align-items:center;gap:18px;margin:10px 0 0 48px;background:#fff;color:#333;font-size:12px;height:34px;padding:0 8px 0 14px;border-radius:3px}
.apply i{width:20px;height:20px;border-radius:50%;background:var(--green);display:flex;align-items:center;justify-content:center}
.field{position:absolute;border:1px solid rgba(255,255,255,.85);color:#fff;font-size:13px;padding:10px 14px;height:42px}
.upload-label{position:absolute;left:641px;top:4645px;font-family:"Rubik",sans-serif;font-weight:500;font-size:21px;color:#fff;white-space:nowrap}
.upload-btn{position:absolute;left:955px;top:4636px;width:145px;height:42px;background:#fff;color:#333;font-size:13px;display:flex;align-items:center;justify-content:center}
.submit{position:absolute;left:641px;top:4814px;width:459px;height:40px;background:var(--blue-light);color:#fff;font-family:"Rubik",sans-serif;font-weight:500;font-size:16px;display:flex;align-items:center;justify-content:center}

/* footer */
.site-footer{top:4872px;height:394px;background:#fff}
.footer-about{position:absolute;left:100px;top:130px;width:310px;font-size:12px;line-height:19px;color:#333;text-align:justify}
.footer-btn{position:absolute;left:100px;top:313px;width:260px;height:40px;background:var(--blue-light);color:#fff;font-size:14px;display:flex;align-items:center;justify-content:space-between;padding:0 24px}
.fcol{position:absolute;top:70px;font-size:14px;color:#333;white-space:nowrap}
.fcol h5{font-family:"Rubik",sans-serif;font-weight:500;font-size:16px;color:var(--blue-light);text-decoration:underline;text-underline-offset:5px;margin-bottom:16px}
.fcol li{list-style:none;line-height:33px}
.contact-li{display:flex;gap:10px;align-items:flex-start;line-height:20px;margin-bottom:18px}
.pin{width:16px;height:16px;border-radius:50%;background:var(--blue-light);flex:none;margin-top:2px}
.cert-badge{position:absolute;left:927px;top:250px;width:145px;height:112px;border:1px solid #bbb;background:#f7f7f7;display:flex;align-items:center;justify-content:center}
.copyright{position:absolute;left:0;top:5266px;width:1200px;height:63px;background:#f1f3f5;text-align:center;line-height:63px;font-size:13px;color:#333;letter-spacing:.5px}
</style>
</head>
<body>

<header class="site-header">
  <div class="topbar">
    <span>☎ 08-512 30 40</span><span>✉ info@tkrclean.se</span><span>⌖ Ängsvägen 12, 123 45 Farsta</span>
    <span class="social"><i class="dot"></i><i class="dot"></i><i class="dot"></i></span>
  </div>
  <div class="logo" style="left:100px;top:24px;font-size:42px"><span class="mark" style="width:40px;height:40px"></span>TKR Clean AB</div>
  <nav class="nav"><a class="active">Hem</a><a>Om oss</a><a>Våra tjänster</a><a>Jobb</a><a>Kontakta oss</a></nav>
</header>

<section class="hero">
  <div class="hero-photo" role="img" aria-label="Mattrengöring med maskin på grå heltäckningsmatta"></div>
  <h1>Fullstädning<br>Tjänster i Stockholm<br>med 24/7 bokning</h1>
  <a class="btn btn-green" style="left:100px;width:222px">Läs mer
    <svg class="arrow-line" viewBox="0 0 40 12"><path d="M0 6h34M28 1l6 5-6 5" stroke="#fff" stroke-width="1.5" fill="none" stroke-dasharray="3 2"/></svg></a>
  <a class="btn btn-blue" style="left:340px;width:223px">Kontakta oss
    <svg class="arrow-line" viewBox="0 0 40 12"><path d="M0 6h34M28 1l6 5-6 5" stroke="#fff" stroke-width="1.5" fill="none" stroke-dasharray="3 2"/></svg></a>
  <div class="dots"><span class="on"></span><span></span><span></span><span></span></div>
  <svg class="wave" width="1200" height="140" viewBox="0 0 1200 140">
    <path d="M0 40 C300 140 600 110 850 70 C1000 45 1120 60 1200 20 V140 H0Z" fill="var(--blue-light)"/>
    <path d="M0 55 C300 150 600 120 850 82 C1000 58 1120 70 1200 34 V140 H0Z" fill="var(--green)"/>
    <path d="M0 72 C300 160 600 130 850 96 C1000 74 1120 86 1200 52 V140 H0Z" fill="#fff"/>
  </svg>
</section>

<section class="about">
  <svg class="about-ring" width="436" height="436" viewBox="0 0 436 436"><path d="M218 4 A214 214 0 1 1 40 330" stroke="var(--green)" stroke-width="8" fill="none"/></svg>
  <div class="about-photo" role="img" aria-label="Fönsterputsare i skylift vid glasfasad"></div>
  <div class="about-text">
    <h2>OM VÅRT FÖRETAG</h2>
    <h3>VÄLKOMMEN TILL TKR CLEAN AB</h3>
    <p class="body">Lorem Ipsum är helt enkelt dummy text från trycker- och sättningsindustrin. Lorem Ipsum har varit branschens vanliga dummytext ända sedan 1500-talet, då en okänd skrivare tog ett pentry av typ och förvrängde det för att göra en typprovbok. Den har överlevt inte bara fem århundraden, utan också språnget till elektronisk sättning, förblir i stort sett oförändrad.</p>
    <p class="body">Det blev populärt på 1960-talet med lanseringen av tryckark som innehåller Lorem Ipsum-passager, och mer nyligen med programvara för desktop publishing som vanliga layoutprogram inklusive versioner av Lorem Ipsum. Lorem Ipsum har varit branschens vanliga dummytext ända sedan 1500-talet, då en okänd skrivare tog ett pentry av typ och förvrängde det för att göra en typprovbok.</p>
    <a class="btn-sm">LÄS MER <svg width="30" height="10" viewBox="0 0 30 10"><path d="M0 5h25M21 1l4 4-4 4" stroke="#fff" fill="none" stroke-dasharray="3 2"/></svg></a>
  </div>
</section>

<section class="staff">
  <svg class="hand-icon abs" style="left:570px;top:112px" width="60" height="56" viewBox="0 0 60 56"><path d="M14 50 L8 30 C6 24 12 22 14 27 L18 36 L22 12 C23 7 29 8 28 13 L27 30 L33 8 C34 3 40 4 39 9 L35 30 L42 14 C44 10 49 12 47 17 L40 36 C38 46 32 52 24 52Z" fill="var(--green)"/><circle cx="48" cy="6" r="4" fill="var(--green)"/><circle cx="54" cy="16" r="3" fill="var(--green)"/></svg>
  <h2 class="sec-title abs" style="left:0;width:1200px;top:172px">OM VÅR PERSONAL</h2>
  <p class="sec-sub abs" style="left:0;width:1200px;top:228px">Våra senaste erbjudanden och tjänster som vi tillhandahåller av expertteam</p>
  <svg class="chev" style="left:46px" width="16" height="28" viewBox="0 0 16 28"><path d="M14 2 2 14l12 12" stroke="#999" stroke-width="2" fill="none"/></svg>
  <svg class="chev" style="left:1130px" width="16" height="28" viewBox="0 0 16 28"><path d="M2 2l12 12L2 26" stroke="#999" stroke-width="2" fill="none"/></svg>
  <div class="staff-cards">
    <div class="card"><div class="avatar" role="img" aria-label="Porträtt av Johan Lindqvist"></div><h4>Johan Lindqvist</h4><p class="role">VD / Grundare</p><p class="tel">Tel: 08 – 512 30 40</p><div class="socials"><span></span><span></span><span></span></div></div>
    <div class="card"><div class="avatar" role="img" aria-label="Porträtt av Maria Ekholm"></div><h4>Maria Ekholm</h4><p class="role">Ekonomi &amp; inköp</p><p class="tel">Tel: 08 – 512 30 41</p><div class="socials"><span></span><span></span><span></span></div></div>
    <div class="card"><div class="avatar" role="img" aria-label="Porträtt av Erik Sandberg"></div><h4>Erik Sandberg</h4><p class="role">Personal &amp; löner</p><p class="tel">Tel: 08 – 512 30 42</p><div class="socials"><span></span><span></span><span></span></div></div>
    <div class="card"><div class="avatar" role="img" aria-label="Porträtt av Lena Forsberg"></div><h4>Lena Forsberg</h4><p class="role">Drift &amp; försäljning</p><p class="tel">Tel: 08 – 512 30 43</p><div class="socials"><span></span><span></span><span></span></div></div>
  </div>
</section>

<section class="services">
  <div class="services-bg"></div>
  <svg class="abs" style="left:0;top:0" width="1200" height="150" viewBox="0 0 1200 150">
    <path d="M0 0 H1200 V40 C1000 120 760 60 560 90 C360 120 180 40 0 110Z" fill="var(--grey-bg)"/>
    <path d="M0 110 C180 40 360 120 560 90 C760 60 1000 120 1200 40 V62 C1000 140 760 82 560 110 C360 138 180 64 0 130Z" fill="var(--green)"/>
  </svg>
  <svg class="hand-icon abs" style="left:570px;top:142px" width="60" height="56" viewBox="0 0 60 56"><path d="M14 50 L8 30 C6 24 12 22 14 27 L18 36 L22 12 C23 7 29 8 28 13 L27 30 L33 8 C34 3 40 4 39 9 L35 30 L42 14 C44 10 49 12 47 17 L40 36 C38 46 32 52 24 52Z" fill="var(--green)"/><circle cx="48" cy="6" r="4" fill="var(--green)"/><circle cx="54" cy="16" r="3" fill="var(--green)"/></svg>
  <h2 class="sec-title abs" style="left:0;width:1200px;top:200px">VÅRA TJÄNSTER</h2>
  <p class="sec-sub abs" style="left:0;width:1200px;top:262px">Hur dina bästa städexperter gör våra bästa städtjänster åt dig!</p>
  <div class="svc" style="left:106px"><div class="svc-photo" role="img" aria-label="Hink med städredskap och rengöringsmedel"></div><div class="svc-icon"><svg width="30" height="30" viewBox="0 0 30 30"><path d="M6 24l12-12M16 6l8 8-4 4-8-8z" stroke="#fff" stroke-width="2.5" fill="none"/></svg></div><h3>Daily<br>Cleaning</h3><a class="more">MORE INFO <i><svg width="12" height="12" viewBox="0 0 12 12"><path d="M1 6h9M6 2l4 4-4 4" stroke="var(--green)" stroke-width="2" fill="none"/></svg></i></a></div>
  <div class="svc" style="left:365px"><div class="svc-photo" role="img" aria-label="Golvmopp på blankt golv"></div><div class="svc-icon"><svg width="30" height="30" viewBox="0 0 30 30"><rect x="5" y="14" width="20" height="10" fill="none" stroke="#fff" stroke-width="2.5"/><path d="M15 4v10M10 9h10" stroke="#fff" stroke-width="2.5"/></svg></div><h3>Floor Care<br>Cleaning</h3><a class="more">MORE INFO <i><svg width="12" height="12" viewBox="0 0 12 12"><path d="M1 6h9M6 2l4 4-4 4" stroke="var(--green)" stroke-width="2" fill="none"/></svg></i></a></div>
  <div class="svc" style="left:625px"><div class="svc-photo" role="img" aria-label="Fönsterputsare i rep på fasad" style="background:linear-gradient(160deg,#7d9186,#39514a)"></div><div class="svc-icon"><svg width="30" height="30" viewBox="0 0 30 30"><rect x="6" y="6" width="18" height="18" fill="none" stroke="#fff" stroke-width="2.5"/><path d="M15 6v18M6 15h18" stroke="#fff" stroke-width="2"/></svg></div><h3>Window<br>Cleaning</h3><a class="more">MORE INFO <i><svg width="12" height="12" viewBox="0 0 12 12"><path d="M1 6h9M6 2l4 4-4 4" stroke="var(--green)" stroke-width="2" fill="none"/></svg></i></a></div>
  <div class="svc" style="left:885px"><div class="svc-photo" role="img" aria-label="Mattrengöring med sugmunstycke" style="background:linear-gradient(160deg,#8a8b8c,#4e5052)"></div><div class="svc-icon"><svg width="30" height="30" viewBox="0 0 30 30"><path d="M8 24V10a5 5 0 0 1 10 0v4M8 24h16" stroke="#fff" stroke-width="2.5" fill="none"/></svg></div><h3>Carpet<br>Cleaning</h3><a class="more">MORE INFO <i><svg width="12" height="12" viewBox="0 0 12 12"><path d="M1 6h9M6 2l4 4-4 4" stroke="var(--green)" stroke-width="2" fill="none"/></svg></i></a></div>
</section>

<section class="ambitions">
  <svg class="hand-icon abs" style="left:570px;top:50px" width="60" height="56" viewBox="0 0 60 56"><path d="M14 50 L8 30 C6 24 12 22 14 27 L18 36 L22 12 C23 7 29 8 28 13 L27 30 L33 8 C34 3 40 4 39 9 L35 30 L42 14 C44 10 49 12 47 17 L40 36 C38 46 32 52 24 52Z" fill="var(--green)"/><circle cx="48" cy="6" r="4" fill="var(--green)"/><circle cx="54" cy="16" r="3" fill="var(--green)"/></svg>
  <h2 class="sec-title abs" style="left:0;width:1200px;top:112px;color:var(--blue-light)">VÅRA AMBITIONER OCH STÖDJANDE</h2>
  <p class="sec-sub abs" style="left:0;width:1200px;top:168px">I vårt arbete för dig använder våra städexperter endast miljövänliga material</p>
  <div class="amb-cards">
    <div class="amb"><svg width="70" height="82" viewBox="0 0 70 82" fill="none" stroke="var(--green)" stroke-width="2.5"><circle cx="35" cy="32" r="26"/><circle cx="35" cy="32" r="18"/><path d="M20 56l-6 22 12-6 6 8 3-22M50 56l6 22-12-6-6 8"/></svg>Quality</div>
    <div class="amb"><svg width="82" height="82" viewBox="0 0 82 82" fill="none" stroke="var(--green)" stroke-width="2.5"><circle cx="41" cy="46" r="30"/><path d="M16 36c10 4 14 0 22 6s4 14 12 16M48 18c0 8 8 10 14 12"/><path d="M40 14c4-10 14-12 18-10-2 8-8 12-18 10zM40 14c-4-8-12-10-16-8 2 6 8 10 16 8z"/></svg>Environment</div>
    <div class="amb"><svg width="70" height="82" viewBox="0 0 70 82" fill="none" stroke="var(--green)" stroke-width="2.5"><path d="M16 26a19 19 0 0 1 38 0zM12 26h46"/><path d="M22 30v6a13 13 0 0 0 26 0v-6"/><path d="M8 80V66c0-8 12-14 27-14s27 6 27 14v14zM35 52v28"/></svg>Labour Conditions</div>
    <div class="amb"><svg width="76" height="82" viewBox="0 0 76 82" fill="none" stroke="var(--green)" stroke-width="2.5"><path d="M8 4h40l10 10v42M8 4v74h40"/><path d="M16 20h28M16 30h28M16 40h20M16 50h16"/><circle cx="56" cy="56" r="12"/><path d="M50 66l-2 14 8-4 8 4-2-14"/></svg>Certificates</div>
  </div>
</section>

<div class="sector" style="left:100px;top:3262px">
  <h2>Tjänster offentlig sektor</h2>
  <p class="body">Lorem Ipsum är helt enkelt dummy text från trycker- och sättningsindustrin. Lorem Ipsum har varit branschens vanliga dummytext ända sedan 1500-talet, då en okänd skrivare tog ett pentry av typ och förvrängde det för att göra en typprovbok. Den har överlevt inte bara fem århundraden, utan också språnget till elektronisk sättning, förblir i stort sett oförändrad.</p>
  <p class="body">Det blev populärt på 1960-talet med lanseringen av tryckark som innehåller Lorem Ipsum-passager, och mer nyligen med programvara för desktop publishing som vanliga layoutprogram inklusive versioner av Lorem Ipsum. Lorem Ipsum har varit branschens vanliga dummytext ända sedan 1500-talet, då en okänd skrivare tog ett pentry av typ och förvrängde det för att göra en typprovbok.</p>
</div>
<div class="sector-photo" style="left:600px;top:3275px;background:linear-gradient(160deg,#8fa0a8,#c85a2a 45%,#6c6f70)" role="img" aria-label="Orange sopmaskin rengör gata"></div>

<div class="sector-photo" style="left:100px;top:3621px;background:linear-gradient(150deg,#b7c9d6,#3f5f7c 55%,#9bb4c6)" role="img" aria-label="Fönsterputsare rengör glasfasad"></div>
<div class="sector" style="left:630px;top:3608px;width:472px">
  <h2>Tjänster privat sektor</h2>
  <p class="body">Lorem Ipsum är helt enkelt dummy text från trycker- och sättningsindustrin. Lorem Ipsum har varit branschens vanliga dummytext ända sedan 1500-talet, då en okänd skrivare tog ett pentry av typ och förvrängde det för att göra en typprovbok. Den har överlevt inte bara fem århundraden, utan också språnget till elektronisk sättning, förblir i stort sett oförändrad.</p>
  <p class="body">Det blev populärt på 1960-talet med lanseringen av tryckark som innehåller Lorem Ipsum-passager, och mer nyligen med programvara för desktop publishing som vanliga layoutprogram inklusive versioner av Lorem Ipsum. Lorem Ipsum har varit branschens vanliga dummytext ända sedan 1500-talet, då en okänd skrivare tog ett pentry av typ och förvrängde det för att göra en typprovbok.</p>
</div>

<div class="sector" style="left:100px;top:3960px">
  <h2>Tjänster husägare sektor</h2>
  <p class="body">Lorem Ipsum är helt enkelt dummy text från trycker- och sättningsindustrin. Lorem Ipsum har varit branschens vanliga dummytext ända sedan 1500-talet, då en okänd skrivare tog ett pentry av typ och förvrängde det för att göra en typprovbok. Den har överlevt inte bara fem århundraden, utan också språnget till elektronisk sättning, förblir i stort sett oförändrad.</p>
  <p class="body">Det blev populärt på 1960-talet med lanseringen av tryckark som innehåller Lorem Ipsum-passager, och mer nyligen med programvara för desktop publishing som vanliga layoutprogram inklusive versioner av Lorem Ipsum. Lorem Ipsum har varit branschens vanliga dummytext ända sedan 1500-talet, då en okänd skrivare tog ett pentry av typ och förvrängde det för att göra en typprovbok.</p>
</div>
<div class="sector-photo" style="left:600px;top:3972px;background:linear-gradient(160deg,#dfe8f0,#e4c04a 50%,#9dc3e0)" role="img" aria-label="Förälder och barn städar hemma"></div>

<section class="jobs">
  <div class="jobs-left"></div>
  <div class="jobs-right"></div>
  <div class="panel-title" style="left:100px;top:50px"><svg width="44" height="42" viewBox="0 0 60 56"><path d="M14 50 L8 30 C6 24 12 22 14 27 L18 36 L22 12 C23 7 29 8 28 13 L27 30 L33 8 C34 3 40 4 39 9 L35 30 L42 14 C44 10 49 12 47 17 L40 36 C38 46 32 52 24 52Z" fill="#fff"/></svg>Aktuell öppning</div>
  <div class="panel-title" style="left:645px;top:50px"><svg width="44" height="42" viewBox="0 0 60 56"><path d="M14 50 L8 30 C6 24 12 22 14 27 L18 36 L22 12 C23 7 29 8 28 13 L27 30 L33 8 C34 3 40 4 39 9 L35 30 L42 14 C44 10 49 12 47 17 L40 36 C38 46 32 52 24 52Z" fill="#fff"/></svg>Skicka in ditt cv</div>
  <div class="job" style="top:118px"><span class="num">1.</span><h4>General Manager</h4><p>Lorem ipsum är helt enkelt dummy text från trycker- och sättningsindustrin. Lorem Ipsum har varit branschens</p><a class="apply">Ansök nu <i><svg width="10" height="10" viewBox="0 0 12 12"><path d="M1 6h9M6 2l4 4-4 4" stroke="#fff" stroke-width="2" fill="none"/></svg></i></a></div>
  <div class="job" style="top:256px"><span class="num">2.</span><h4>Rengöringsmedel</h4><p>Lorem ipsum är helt enkelt dummy text från trycker- och sättningsindustrin. Lorem Ipsum har varit branschens</p><a class="apply">Ansök nu <i><svg width="10" height="10" viewBox="0 0 12 12"><path d="M1 6h9M6 2l4 4-4 4" stroke="#fff" stroke-width="2" fill="none"/></svg></i></a></div>
  <div class="job" style="top:394px"><span class="num">3.</span><h4>Revisor</h4><p>Lorem ipsum är helt enkelt dummy text från trycker- och sättningsindustrin. Lorem Ipsum har varit branschens</p><a class="apply">Ansök nu <i><svg width="10" height="10" viewBox="0 0 12 12"><path d="M1 6h9M6 2l4 4-4 4" stroke="#fff" stroke-width="2" fill="none"/></svg></i></a></div>
</section>
<div class="field" style="left:641px;top:4444px;width:459px">Förnamn</div>
<div class="field" style="left:641px;top:4504px;width:459px">Efternamn</div>
<div class="field" style="left:641px;top:4566px;width:230px">E-post</div>
<div class="field" style="left:881px;top:4566px;width:219px">Telefon</div>
<div class="upload-label">Attatched Your Resume</div>
<div class="upload-btn">Upload Your CV</div>
<div class="field" style="left:641px;top:4703px;width:459px;height:94px">Meddelande</div>
<div class="submit">Skicka</div>

<footer class="site-footer">
  <div class="logo" style="left:108px;top:50px;font-size:40px"><span class="mark" style="width:36px;height:36px"></span>TKR Clean AB</div>
  <p class="footer-about">Lorem Ipsum är helt enkelt dummy text från trycker- och sättningsindustrin. Lorem Ipsum har varit branschens vanliga dummytext ända sedan 1500-talet, då en okänd skrivare tog ett pentry av typ och förvrängde det för att göra en typprovbok. Den har överlevt inte bara fem århundraden, utan också språnget till elektronisk sättning, förblivit i stort sett oförändrad.</p>
  <a class="footer-btn">Begär ett möte <span>→</span></a>
  <div class="fcol" style="left:482px"><h5>Snabblänkar</h5><ul><li>Hem</li><li>Om oss</li><li>Våra tjänster</li><li>Jobb</li><li>Kontakta oss</li></ul></div>
  <div class="fcol" style="left:687px"><h5>Våra tjänster</h5><ul><li>Daily Cleaning</li><li>Floor Care</li><li>Window Cleaning</li><li>Carpet Cleaning</li></ul>
    <h5 style="margin-top:40px">Sociala media</h5><div style="display:flex;gap:8px"><i class="dot" style="background:var(--green)"></i><i class="dot" style="background:var(--green)"></i><i class="dot" style="background:var(--green)"></i></div></div>
  <div class="fcol" style="left:919px"><h5>Kontakter</h5>
    <div class="contact-li"><span class="pin"></span>08-512 30 40</div>
    <div class="contact-li"><span class="pin"></span>info@tkrclean.se</div>
    <div class="contact-li"><span class="pin"></span>Ängsvägen 12<br>123 45 Farsta</div>
  </div>
  <div class="cert-badge" role="img" aria-label="Certifieringsmärke"><svg width="70" height="70" viewBox="0 0 70 70"><circle cx="35" cy="35" r="30" fill="none" stroke="#999" stroke-width="3"/></svg></div>
</footer>
<div class="copyright">© COPYRIGHT - 2012 TKR CLEAN AB &nbsp;|&nbsp; ALL RIGHTS RESERVED</div>

</body>
</html>
```